依頼詳細
■コンペで依頼するもの
・トップページ(ワイヤーフレーム参照)
■当選後に依頼するもの
・第2階層ページ(ワイヤーフレーム参照)
・記事ページ(ワイヤーフレーム参照)
・アイキャッチ画像6種類

当選後、追加依頼をプロジェクト形式で発注しますので、受注できる方でお願いします。
追加依頼の予算は4万円以内です。
サイトURL
http://www.morinoyashiro-sample.jp/wp/
ページ数
1ページ
希望イメージ
シンプル 複雑
単色 カラフル
暗い 明るい
日常 高級
遊び心 厳粛
未来的 伝統的
女性的 男性的
希望する色
背景は白指定です。他はお任せします。
納品ファイル
• フォトショップ形式 (.psd)
• PNG形式 (.png)
補足説明
■参考サイト
http://kotobukisha-example.or.jp/jingu/
http://www.hanazakura-example.or.jp/top.php
http://fukuo-mitama.or.jp/

■素材
添付のワイヤーフレームと写真です。
写真は次のアドレスからダウンロードしてください。
http://pelotix.net/morinoyashiro/sozai.zip
現行サイトの画像も利用して頂いて構いません。

※メニュー部の配置は自由にして頂いて構いません。
※ボックス内の文字は画像データとして利用します。他の文字はテキストデータで利用します。
※他有料素材も5千円程度まではお支払できます。

神紋(ロゴマーク)の色は自由に設定して頂いて構いません。
深緑以外であれば問題ないようです。
現行サイトのロゴには「北原郷総鎮守」が含まれています。
ですが、今回はトップページから削除することが決定しています。
説明が不足しておりまして申し訳ございません。
ワイヤーフレーム内、サイトマップのテキストは確定していません。
デザインが分かれば大丈夫です。ダミーのテキストを入れてください。
レスポンシブ対応とありますが、対応は当方で行います。
今回、PC版トップページのイメージアップが最優先ですので、
コンペではレスポンシブを意識せずにデザインして頂いて構いません。
よろしくお願いします。
23日(月) 14:00より選考を開始します。
一時停止の理由:たくさんのご提案を頂きましてありがとうございました。
現在クライアントを含めた席で協議中ですが、どれもクオリティが高く難航しています。
本日中には決定する見込みです。

全体の配色、写真の扱い方を考慮した結果、「クライアントのイメージに近い」という事で選択させて頂きました。

沢山のご提案、誠にありがとうございました。

```html
<!DOCTYPE html>
<html lang="ja">
<head>
<meta charset="utf-8">
<title>森乃社 トップページ</title>
<link href="https://fonts.googleapis.com/css2?family=Noto+Serif+JP:wght@400;600;700&family=Noto+Sans+JP:wght@400;500;700&display=swap" rel="stylesheet">
<style>
:root{
  --red:#a8262b;
  --ink:#2b2622;
  --muted:#7a716a;
  --line:#ddd6cc;
  --paper:#ffffff;
  --cream:#f6f1e8;
  --foot:#ecebe8;
  --dark:#1b1917;
  --forest1:#2f3d22;
  --forest2:#6f7d4c;
  --forest3:#c9cfa9;
}
*{margin:0;padding:0;box-sizing:border-box}
html,body{width:831px;height:1200px;overflow:hidden;background:var(--paper)}
body{font-family:"Noto Sans JP",sans-serif;color:var(--ink);font-size:10px;position:relative}
.site-header{height:50px;display:flex;align-items:center;justify-content:space-between;padding:0 22px;border-bottom:1px solid var(--line)}
.brand{display:flex;align-items:center;gap:8px;font-family:"Noto Serif JP",serif;font-weight:700;font-size:20px;color:var(--red);letter-spacing:3px}
.brand-dot{width:22px;height:22px;border-radius:50%;background:var(--red)}
.util-nav{display:flex;align-items:center;gap:12px;font-size:9px;color:var(--muted)}
.util-nav span::before{content:"●";color:var(--red);font-size:6px;margin-right:3px;vertical-align:middle}
.search{display:flex;align-items:center;gap:4px}
.search-field{width:70px;height:16px;border:1px solid var(--line)}
.search-btn{background:var(--muted);color:#fff;padding:2px 6px;font-size:8px}
.hero{position:absolute;top:50px;left:0;width:831px;height:380px;background:
  radial-gradient(ellipse at 48% 75%,#e8ead2 0%,rgba(232,234,210,0) 35%),
  linear-gradient(90deg,var(--forest1) 0%,var(--forest2) 25%,var(--forest3) 50%,var(--forest2) 75%,var(--forest1) 100%)}
.hero-copy{position:absolute;top:36px;left:170px;display:flex;flex-direction:row-reverse;align-items:flex-start;gap:12px;font-family:"Noto Serif JP",serif;color:#fff;text-shadow:0 0 6px rgba(0,0,0,.35)}
.hero-copy span{writing-mode:vertical-rl;white-space:nowrap;line-height:1}
.hero-copy .lead{font-size:26px;letter-spacing:4px}
.hero-copy .lead.second{margin-top:46px}
.hero-copy .sub{font-size:13px;letter-spacing:3px;opacity:.9;margin-top:96px}
.global-nav{position:absolute;top:405px;left:60px;width:711px;height:70px;display:flex;gap:4px}
.gnav-item{flex:1;min-width:0;background:var(--paper);border:1px solid var(--line);display:flex;flex-direction:column;align-items:center;justify-content:center;gap:4px}
.gnav-item .jp{font-family:"Noto Serif JP",serif;font-weight:600;font-size:10px;white-space:nowrap;display:flex;align-items:center;gap:4px}
.gnav-item .jp::before{content:"";width:11px;height:11px;border-radius:50%;background:var(--red);flex:none}
.gnav-item .en{font-size:7px;color:var(--muted);letter-spacing:1px}
.sidebar{position:absolute;top:500px;left:60px;width:205px}
.section-title{font-family:"Noto Serif JP",serif;font-weight:700;font-size:13px;display:flex;align-items:center;gap:6px;padding-bottom:6px;border-bottom:2px solid var(--red)}
.section-title::before{content:"";width:14px;height:14px;border-radius:50%;background:var(--red)}
.events{border:1px solid var(--line);border-top:none;padding:4px 10px 8px}
.event{padding:5px 0;border-bottom:1px dotted var(--line);font-size:8.5px;line-height:1.5}
.event .date{color:var(--muted)}
.more{text-align:right;font-size:8px;color:var(--muted);margin-top:6px}
.side-banners{margin-top:36px;display:flex;flex-direction:column;gap:8px}
.side-banner{height:66px;background:linear-gradient(120deg,#3b2f28,#8a6a4f 60%,#d9c4a4)}
.side-banner:nth-child(2){background:linear-gradient(120deg,#e9e3d6,#b7a78a)}
.side-banner:nth-child(3){background:linear-gradient(120deg,#3a2a22,#7b4a38 55%,#c99a6e)}
.main{position:absolute;top:500px;left:282px;width:489px}
.feature-banner{height:62px;display:flex}
.feature-banner .label{width:50%;background:var(--cream);display:flex;flex-direction:column;justify-content:center;padding:0 12px;font-family:"Noto Serif JP",serif;font-weight:700;font-size:12px}
.feature-banner .label small{font-family:"Noto Sans JP",sans-serif;font-weight:400;font-size:8px;color:var(--muted);margin-top:3px}
.feature-banner .photo{flex:1;background:linear-gradient(90deg,#7a5b3a,#c9a774 50%,#6e4f34)}
.news{margin-top:40px}
.news .section-title .link{margin-left:auto;font-family:"Noto Sans JP",sans-serif;font-weight:400;font-size:8px;color:var(--muted)}
.news-item{display:flex;gap:22px;padding:6px 8px;border-bottom:1px dotted var(--line);font-size:8.5px}
.news-item .date{color:var(--muted);width:80px}
.cards{margin-top:16px;display:grid;grid-template-columns:repeat(3,1fr);gap:14px 12px}
.card-photo{height:85px;background:linear-gradient(135deg,#8b2a22,#d98a5a 60%,#f0d7b0)}
.card:nth-child(2) .card-photo{background:linear-gradient(135deg,#3f4a2f,#a8a98a 60%,#e5e1cf)}
.card:nth-child(3) .card-photo{background:linear-gradient(135deg,#4e3b2e,#b39273 60%,#e8d8c0)}
.card:nth-child(4) .card-photo{background:linear-gradient(135deg,#3a4a3a,#8c9a85 60%,#d6d8cb)}
.card:nth-child(5) .card-photo{background:linear-gradient(135deg,#5b4630,#c7ab84 60%,#eadfca)}
.card:nth-child(6) .card-photo{background:linear-gradient(135deg,#2e3d52,#8c9fb8 55%,#d98c6a)}
.card p{font-size:8px;line-height:1.5;margin-top:5px;color:#4a433e}
.sitemap{position:absolute;top:1020px;left:0;width:831px;height:100px;background:var(--foot);padding:12px 60px;display:flex;justify-content:space-between}
.sitemap-col h3{font-size:8.5px;font-weight:500;margin-bottom:5px}
.sitemap-col h3::before{content:"▸";color:var(--red);margin-right:3px}
.sitemap-col li{list-style:none;font-size:7.5px;color:var(--muted);line-height:1.7;padding-left:8px}
.sub-links{position:absolute;top:1120px;left:0;width:831px;height:20px;background:#d9d7d3;display:flex;align-items:center;gap:14px;padding:0 60px;font-size:7.5px;color:#555}
.site-footer{position:absolute;top:1140px;left:0;width:831px;height:60px;background:var(--dark);display:flex;align-items:center;justify-content:center;gap:18px;color:#bbb;font-size:8px}
.site-footer .brand{font-size:14px;color:#fff;letter-spacing:2px}
.site-footer .brand-dot{width:16px;height:16px}
.copyright{position:absolute;right:60px;bottom:8px;font-size:7px;color:#888}
</style>
</head>
<body>
<header class="site-header">
  <div class="brand"><span class="brand-dot"></span>森乃社</div>
  <nav class="util-nav">
    <span>アクセス・駐車場</span><span>よくあるご質問</span><span>お問い合わせ</span><span>奉納のご案内</span><span>採用情報</span>
    <div class="search"><div class="search-field"></div><div class="search-btn">検索</div></div>
  </nav>
</header>

<div class="hero" role="img" aria-label="木立に囲まれた参道の写真">
  <div class="hero-copy">
    <span class="lead">神代から</span>
    <span class="lead second">奈良・平安時代への</span>
    <span class="sub">悠久のときを今に伝える杜</span>
  </div>
</div>

<nav class="global-nav">
  <div class="gnav-item"><span class="jp">森乃社について</span><span class="en">ABOUT</span></div>
  <div class="gnav-item"><span class="jp">参拝・ご祈祷</span><span class="en">WORSHIP</span></div>
  <div class="gnav-item"><span class="jp">御祈祷・その他祭事</span><span class="en">PRAYER</span></div>
  <div class="gnav-item"><span class="jp">境内・宝物館</span><span class="en">PRECINCT</span></div>
  <div class="gnav-item"><span class="jp">祭り・神事</span><span class="en">FESTIVAL</span></div>
  <div class="gnav-item"><span class="jp">交通</span><span class="en">ACCESS</span></div>
</nav>

<aside class="sidebar">
  <h2 class="section-title">行事予定</h2>
  <div class="events">
    <div class="event"><div class="date">平成26年6月15日(日)</div>例祭 行事名が入ります</div>
    <div class="event"><div class="date">平成26年6月20日(金)</div>神事 行事名が入ります</div>
    <div class="event"><div class="date">平成26年6月30日(月)</div>大祓式 行事名が入ります</div>
    <div class="event"><div class="date">平成26年7月1日(火)</div>月次祭 行事名が入ります</div>
    <div class="event"><div class="date">平成26年7月7日(月)</div>七夕祭 行事名が入ります</div>
    <div class="event"><div class="date">平成26年7月15日(火)</div>例祭 行事名が入ります</div>
    <div class="more">› 一覧へ</div>
  </div>
  <div class="side-banners">
    <div class="side-banner" role="img" aria-label="社殿の案内バナー写真"></div>
    <div class="side-banner" role="img" aria-label="授与品の案内バナー写真"></div>
    <div class="side-banner" role="img" aria-label="祭事の案内バナー写真"></div>
  </div>
</aside>

<main class="main">
  <div class="feature-banner">
    <div class="label">御祈祷・その他祭事のご案内<small>初宮詣・七五三・厄除など各種ご祈祷</small></div>
    <div class="photo" role="img" aria-label="御祈祷を受ける参拝者の写真"></div>
  </div>

  <section class="news">
    <h2 class="section-title">最新情報<span class="link">› 一覧を見る</span></h2>
    <div class="news-item"><span class="date">平成26年6月10日</span>大祓式のご案内と人形の受付を開始しました</div>
    <div class="news-item"><span class="date">平成26年6月5日</span>境内整備のお知らせ</div>
    <div class="news-item"><span class="date">平成26年6月1日</span>宝物館の開館時間について</div>
  </section>

  <section class="cards">
    <article class="card"><div class="card-photo" role="img" aria-label="楼門の写真"></div><p>この文章はダミーです。文字の大きさや量を確認するために入れています。</p></article>
    <article class="card"><div class="card-photo" role="img" aria-label="参道の写真"></div><p>この文章はダミーです。文字の大きさや量を確認するために入れています。</p></article>
    <article class="card"><div class="card-photo" role="img" aria-label="祭事の写真"></div><p>この文章はダミーです。文字の大きさや量を確認するために入れています。</p></article>
    <article class="card"><div class="card-photo" role="img" aria-label="境内の社の写真"></div><p>この文章はダミーです。文字の大きさや量を確認するために入れています。</p></article>
    <article class="card"><div class="card-photo" role="img" aria-label="拝殿の写真"></div><p>この文章はダミーです。文字の大きさや量を確認するために入れています。</p></article>
    <article class="card"><div class="card-photo" role="img" aria-label="船上祭の写真"></div><p>この文章はダミーです。文字の大きさや量を確認するために入れています。</p></article>
  </section>
</main>

<footer>
  <div class="sitemap">
    <div class="sitemap-col"><h3>トップページ</h3><ul><li>ページ名</li><li>ページ名</li><li>ページ名</li></ul></div>
    <div class="sitemap-col"><h3>森乃社について</h3><ul><li>ページ名</li><li>ページ名</li><li>ページ名</li><li>ページ名</li></ul></div>
    <div class="sitemap-col"><h3>参拝・ご祈祷</h3><ul><li>ページ名</li><li>ページ名</li><li>ページ名</li><li>ページ名</li></ul></div>
    <div class="sitemap-col"><h3>御祈祷・その他祭事</h3><ul><li>ページ名</li><li>ページ名</li><li>ページ名</li><li>ページ名</li></ul></div>
    <div class="sitemap-col"><h3>境内・宝物館</h3><ul><li>ページ名</li><li>ページ名</li><li>ページ名</li><li>ページ名</li></ul></div>
    <div class="sitemap-col"><h3>祭り・神事</h3><ul><li>ページ名</li><li>ページ名</li><li>ページ名</li><li>ページ名</li></ul></div>
  </div>
  <div class="sub-links"><span>アクセス・駐車場</span><span>よくあるご質問</span><span>お問い合わせ</span><span>サイトマップ</span><span>個人情報保護方針</span></div>
  <div class="site-footer">
    <div class="brand"><span class="brand-dot"></span>森乃社</div>
    <span>〒000-0000 北原郷森乃町1-1　TEL 000-000-0000　FAX 000-000-0000</span>
    <span class="copyright">Copyright © Morinoyashiro. All Rights Reserved.</span>
  </div>
</footer>
</body>
</html>
```